Commercial/Corporate Law Firm needs Website Design

Hi guys. I've started up a new law firm and would love your help designing an attractive website. I'll need both design and coding, and to make it easy for us to edit as necessary later, I think it should be built off a Wordpress.org structure.
FIRST IMPRESSIONS
It's very important that the first impression of the website really captures our prospective clients' attention and impresses them. Their first three seconds needs to be good.
I imagine the homepage may be short, with a menu bar and a compelling image, and with a tagline overlaid or underneath (eg. "It's about results.")
The image should be related to our practice areas: eg. IPOs, corporate transactions, or commercial negotiations.
I have previously suggested there could be a skyline image of Sydney or Adelaide. However, because we are based in Adelaide, I don't think Sydney is appropriate - and Adelaide is probably too boring to use.
HOMEPAGE
Being a new firm, we don't have many existing testimonials, and I will be the only lawyer to start with. So we need to focus on the nature of the services we will provide and how my experience can help them. We have an existing logo to use, and I would like the website colour scheme not to clash with that logo (dark blue and white).
After the initial image and tagline there should be a brief introduction to each of the main areas of work, eg. "We specialise in three main areas of practice:"
1. Corporate Transactions and Regulation
2. Business Law and Dispute Resolution
3. Migration Assistance
These should each have an appropriate photo and link to a separate page that briefly describes our services in that area.
Below that there should be a message from me with a photo. Finally, at the bottom, there should be a "Contact Us" section which shows a Google image of our address, contact details, and then our logo with colours inverted.
OTHER PAGES
While we will need some other pages, they should all be fairly simple. I think we will need one page to say "About Us", where I will put information about my experience. I think we will then need one page for each of the 3 areas listed above, which just needs an appropriate image and then text to describe the service. Finally, a "Contact Us" page which I imagine will be the same as the bottom of the homepage.
OTHER DETAILS
For now you can use details from my LinkedIn page to fill out any other text as necessary, or the photo.
Because the logo is square, I would prefer the design of the website also to be rectangular.
Looking forward to seeing your work! Thank you.
Good luck,
Marcus
Target Market(s)
Potential clients:
Businesses with legal issues or disputes
Companies wishing to list on the stock market

```html
<!DOCTYPE html>
<html lang="en">
<head>
<meta charset="utf-8">
<title>Halvorsen Legal</title>
<link rel="stylesheet" href="https://fonts.googleapis.com/css2?family=Lato:ital,wght@0,300;0,400;0,700;0,900;1,700&display=swap">
<style>
:root{
  --navy:#1d3461;
  --navy-dark:#172a4f;
  --ink:#1a1a1a;
  --text:#333;
  --muted:#666;
  --paper:#fff;
  --mist:#f4f4f4;
  --footer:#6b6b6d;
  --black:#050505;
}
*{margin:0;padding:0;box-sizing:border-box}
html,body{width:736px;height:1200px;overflow:hidden}
body{font-family:"Lato",sans-serif;background:var(--paper);color:var(--text);position:relative}
.abs{position:absolute}

/* header */
.site-header{left:0;top:0;width:736px;height:54px;background:var(--navy);box-shadow:0 1px 3px rgba(0,0,0,.4);z-index:2}
.brand{left:96px;top:8px;width:64px;text-align:center;color:var(--paper)}
.brand-mark{display:block;width:18px;height:18px;margin:0 auto 3px;background:var(--paper)}
.brand-name{display:block;font-size:10px;letter-spacing:1px;font-weight:400;line-height:11px}
.brand-sub{display:block;font-size:5px;letter-spacing:3px;font-weight:400;line-height:7px}
.top-contact{right:96px;top:4px;font-size:5.5px;color:var(--paper);display:flex;gap:14px;align-items:center}
.top-contact span{display:flex;align-items:center;gap:2px}
.main-nav{right:108px;top:28px;display:flex;gap:21px;font-size:6.8px;font-weight:700;color:var(--paper);letter-spacing:.2px}
.main-nav span{display:flex;align-items:center;gap:2px}

/* hero */
.hero-photo{left:0;top:54px;width:736px;height:323px;background:linear-gradient(100deg,#5e6d7e 0%,#a8a8a4 25%,#d99a5e 45%,#f2c48a 55%,#4a4b52 70%,#2a2d38 85%,#9ea7b2 100%)}
.hero-caption{left:96px;top:309px;width:545px;height:68px;background:var(--black);border-top:2px solid #6d6d6d;padding:12px 15px 0}
.hero-caption h1{font-size:17px;font-weight:400;color:var(--paper);letter-spacing:.2px;line-height:20px}
.hero-caption p{font-size:5.6px;color:var(--paper);line-height:10px;width:430px;margin-top:2px}
.btn-solid{left:457px;top:25px;width:73px;height:18px;background:var(--navy);color:var(--paper);font-size:5.6px;font-weight:900;display:flex;align-items:center;justify-content:center;border-radius:2px}

/* services */
.section-title{left:0;top:438px;width:736px;text-align:center;font-size:21px;font-weight:300;color:#444;letter-spacing:.5px}
.title-rule{left:316px;top:465px;width:104px;height:8px}
.service{top:479px;width:172px;text-align:center}
.service-photo{width:172px;height:88px}
.service h2{font-size:8.6px;font-weight:700;color:var(--navy);margin-top:7px}
.service p{font-size:5.8px;line-height:10.3px;color:var(--ink);margin-top:2px;padding:0 2px;height:41px;overflow:hidden}
.btn-outline{display:inline-flex;align-items:center;justify-content:center;width:58px;height:15px;border:1.5px solid var(--navy);border-radius:2px;font-size:4.6px;font-weight:900;color:var(--navy);margin-top:12px}

/* about */
.about{left:0;top:714px;width:736px;height:198px;background:var(--mist)}
.portrait{left:96px;top:16px;width:125px;height:147px;border:1.5px solid #999;padding:3px;background:var(--paper)}
.portrait-fill{width:100%;height:100%;background:linear-gradient(180deg,#38414f 0%,#51596a 55%,#1f2838 100%)}
.person{left:96px;top:168px;width:125px;text-align:center}
.person strong{display:block;font-size:8.6px;font-style:italic;font-weight:700;color:#444}
.person span{display:block;font-size:5px;color:var(--muted)}
.about-copy{left:236px;top:36px;width:406px}
.about-copy h2{font-size:19px;font-weight:400;color:#555;line-height:22px}
.about-copy p{font-size:5.9px;line-height:10.3px;color:var(--ink);margin-top:1px}
.about-actions{display:flex;gap:4px;margin-top:8px}
.about-actions .btn-outline{margin-top:0;width:58px;height:15px}
.icon-box{width:16px;height:15px;border:1.5px solid var(--navy);border-radius:2px;display:flex;align-items:center;justify-content:center}
.icon-box i{display:block;width:5px;height:5px;background:var(--navy)}

/* contact band */
.contact-band{left:0;top:912px;width:736px;height:45px;background:var(--navy);display:flex;justify-content:center;align-items:center;gap:22px;color:var(--paper);font-size:14px;font-weight:400}
.contact-band span{display:flex;align-items:center;gap:5px}
.round-icon{width:21px;height:21px;border-radius:50%;background:#7c8290;display:flex;align-items:center;justify-content:center}

.map{left:0;top:957px;width:736px;height:147px;background:linear-gradient(135deg,#e6e6e6,#d4d4d4)}

/* footer */
.site-footer{left:0;top:1104px;width:736px;height:96px;background:var(--footer);color:var(--paper);text-align:center}
.site-footer .brand{position:absolute;left:336px;top:14px}
.footer-links{position:absolute;left:0;top:64px;width:736px;font-size:5.6px;font-weight:700}
.footer-links b{font-weight:400;margin:0 5px}
.copyright{position:absolute;left:0;top:76px;width:736px;font-size:4.4px}
</style>
</head>
<body>

<header class="site-header abs">
  <div class="brand abs">
    <span class="brand-mark"></span>
    <span class="brand-name">HALVORSEN</span>
    <span class="brand-sub">LEGAL</span>
  </div>
  <div class="top-contact abs">
    <span><svg width="5" height="5" viewBox="0 0 10 10"><path d="M2 0l2 2-1 2c1 1 2 2 3 3l2-1 2 2-2 2C4 10 0 6 0 2z" fill="#fff"/></svg>123.456.7890</span>
    <span><svg width="6" height="5" viewBox="0 0 12 9"><rect width="12" height="9" fill="#fff"/><path d="M0 0l6 5 6-5" stroke="#1d3461" fill="none"/></svg>info@HalvorsenLegal.com.au</span>
  </div>
  <nav class="main-nav abs">
    <span>HOME</span><span>ABOUT US</span>
    <span>PRACTICE AREAS <svg width="6" height="4" viewBox="0 0 6 4"><path d="M.5.5l2.5 2.5 2.5-2.5" stroke="#fff" stroke-width="1.2" fill="none"/></svg></span>
    <span>CONTACT US</span>
  </nav>
</header>

<div class="hero-photo abs" role="img" aria-label="Two business people shaking hands in a sunlit city"></div>
<div class="hero-caption abs">
  <h1>WE GET RESULTS!</h1>
  <p>Lorem ipsum dolor sit amet, consectetur adipiscing elit. Sed nec sem mattis, facilisis elit ut, maximus enim. Donec dui sem, fermentum a faucibus ac, tincidunt non ante. Aliquam condiment dapibus orci, vitae mattis ante elementum nec. Sed vulputate vitae turpis ac hendrerit. Nunc pretium mollis elitvol.</p>
  <span class="btn-solid abs">CONTACT US »</span>
</div>

<h2 class="section-title abs">WHAT WE DO</h2>
<svg class="title-rule abs" viewBox="0 0 104 8"><line x1="0" y1="4" x2="44" y2="4" stroke="#555" stroke-width=".8"/><line x1="60" y1="4" x2="104" y2="4" stroke="#555" stroke-width=".8"/><rect x="48" y="0" width="8" height="8" fill="#1d3461"/></svg>

<article class="service abs" style="left:96px">
  <div class="service-photo" role="img" aria-label="Glass office towers against a blue sky" style="background:linear-gradient(135deg,#0d3c8a,#4e94e0 50%,#0b2c6e)"></div>
  <h2>Corporate Transactions &amp; Regulation</h2>
  <p>Lorem ipsum dolor sit amet, consectetur adipiscing elit. Sed nec sem mattis, facilisis elit ut, maximus enim. Donec dui sem, fermentum a faucibus ac, tincidunt non ante aliquam condimentum dapibus orci, vitae mattis ante elementum.</p>
  <span class="btn-outline">LEARN MORE »</span>
</article>
<article class="service abs" style="left:282px">
  <div class="service-photo" role="img" aria-label="Business people discussing documents at a table" style="background:linear-gradient(135deg,#8a6a50,#d9cfc4 50%,#6d5a4c)"></div>
  <h2>Business Law &amp; Dispute Resolution</h2>
  <p>Condimentum dapibus orci, vitae mattis ante elementum nec. Sed vulputate vitae turpis ac hendrerit. Nunc pretium mollis elit, ut volutpat ipsum pretium dictum est vitae erat ultricies posuere aliquam libero posuere mauris porttitor tincidunt</p>
  <span class="btn-outline">LEARN MORE »</span>
</article>
<article class="service abs" style="left:469px">
  <div class="service-photo" role="img" aria-label="Family silhouetted against a sunset sky" style="background:linear-gradient(180deg,#5d7aa8,#f0b060 65%,#7a4020)"></div>
  <h2>Migration Assistance</h2>
  <p>Aliquam libero posuere mauris porttitor tincidunt nibh, et consequat nibh. tincidunt sit amet. Quisque a orci felis. Ut ultrices fermentum risus sit amet eleifend uisque obortis vivamus vel justo id massa gravida vestibulum ellentesque.</p>
  <span class="btn-outline">LEARN MORE »</span>
</article>

<section class="about abs">
  <div class="portrait abs"><div class="portrait-fill" role="img" aria-label="Portrait of the firm's lawyer in a suit"></div></div>
  <div class="person abs"><strong>Marcus Halvorsen</strong><span>Lawyer</span></div>
  <div class="about-copy abs">
    <h2>It's about RESULTS.</h2>
    <p>Lorem ipsum dolor sit amet, consectetur adipiscing elit. Sed nec sem mattis, facilisis elit ut, maximus enim. Donec dui sem, fermentum a faucibus ac, tincidunt non ante aliquam. condimentum dapibus orci, vitae mattis ante elementum nec. Sed vulputate vitae turpis ac hendrerit. Nunc pretium mollis elit, ut volutpat ipsum pretium ac. Nam dictum est vitae erat ultricies, posuere aliquam libero posuere mauris porttitor tincidunt nibh, et consequat nibh. tincidunt sit amet. Quisque a orci felis. Ut ultrices fermentum risus sit amet eleifend. Quisque quis lobortis nulla. Vivamus vel justo id massa. Donec pharetra nibh turpis, id aliquam nibh vehicula blandit. Proin eu odio eu nulla fermentum egestas. In sed congue sem. Fusce porta urna velit, ac vulputate quam pharetra in. Vivamus vel elit sit amet lectus gravida blandit non a felis. Ut vitae mattis sem. Mauris egestas dictum</p>
    <div class="about-actions"><span class="btn-outline">LEARN MORE »</span><span class="icon-box"><i></i></span></div>
  </div>
</section>

<div class="contact-band abs">
  <span><span class="round-icon"><svg width="11" height="11" viewBox="0 0 10 10"><path d="M2 0l2 2-1 2c1 1 2 2 3 3l2-1 2 2-2 2C4 10 0 6 0 2z" fill="#fff"/></svg></span>123.456.7890</span>
  <span><span class="round-icon"><svg width="11" height="8" viewBox="0 0 12 9"><rect width="12" height="9" fill="#fff"/><path d="M0 0l6 5 6-5" stroke="#7c8290" fill="none"/></svg></span>info@HalvorsenLegal.com.au</span>
</div>

<div class="map abs" role="img" aria-label="Street map showing the office location in the city centre"></div>

<footer class="site-footer abs">
  <div class="brand">
    <span class="brand-mark"></span>
    <span class="brand-name">HALVORSEN</span>
    <span class="brand-sub">LEGAL</span>
  </div>
  <div class="footer-links">Home<b>|</b>About Us<b>|</b>Corporate Transactions &amp; Regulation<b>|</b>Business Law &amp; Dispute Resolution<b>|</b>Migration Assistance<b>|</b>Contact Us</div>
  <div class="copyright">©2018 HalvorsenLegal</div>
</footer>

</body>
</html>
```